New CORPORATE WEBSITE DESIGN (Graphic layout for a WEBSITE TEMPLATE required - Photoshop files)

Hi – I need a draft created for a new corporate website for our company.
I need a graphic design concept which can be applied to a whole website layout -
I have a separate web development team who will implement the design onto Wordpress.
We are an Asian Buying Office based in Hong Kong and Shenzhen which facilitates relationships between factories in China and customers (retailers/etailers) all over the world.
We are a “boutique” agency, which offers highly customized services – we are highly consultative in our approach and tailor services to suit the needs of our customers with customized solutions. Our services are transparent partnership- and-integrity-based, and aimed to support at a certain size of company in growth mode.
We have dedicated teams of staff focused entirely on a customer’s business and we work TOGETHER with customers to solve their product design, patent, product engineering, goods production, quality control and supply chain challenges operating in 24/7 through our proprietary web-based supply chain platform called Cargoloom.
I have a PowerPoint which can be used to drive:
1) creative direction (colour palette etc) and to provide basic content for each “screen.” I would like to see design options based on the PowerPoint which offer creative ways to create a new look and feel for us for a corporate website which will not be social media enabled or ecommerce enabled. We do not put ANY customer brand names direct or references on our website – relationships are private. The home page of the website should say in the design style – “product design and branded global consumer goods” as well as “professional engineering and quality control proficiency”.
The website should be clean and functional – have the “usability” of the Pebble website but the “Meridian 300” look & feel of the Tan & Voss website (http://www.tanvoss-example.com/eng/global/home.php) – Tan & Voss is a benchmark for us. Tan & Voss is the largest company in our industry doing what we do.
I do not want to COPY this example - I am offering it as a benchmark for a CLEAN, vibrant, professional site which sends a good brand and services message. The target market is a global B to B market – SMEs who are well funded and growing, brands with growth potential, or large, established brands who are looking to a) build a supply chain partner to help them grow b) increase their revenues by managing their costs c) reduce their risk through an experience buyer’s agent such as ourselves – a partner with integrity who they can trust. The web site design must say “global consumer brands” WITHOUT DIRECTLY ALLUDING TO THE LOGOS AND/OR BRAND NAMES WE WORK WITH , " full service agency – managing the process from product design and engineering, quality control and risk management to product manufacturing and shipping logistics" and “accountability/integrity/transparency within the partnership.” Designer to choose colors to be used in the design - I have also attached my logo file to allow you to select a color palette which will be complementary.
PLEASE FEEL FREE TO ASK ANY QUESTIONS - I AM HAPPY TO PROVIDE MORE DETAILS.

```html
<!DOCTYPE html>
<html lang="en">
<head>
<meta charset="utf-8">
<title>Company – Orvane Trading Limited</title>
<link rel="stylesheet" href="https://fonts.googleapis.com/css2?family=Arimo:wght@400;700&display=swap">
<style>
:root{
  --navy:#0b2a63;
  --navy-deep:#071c42;
  --blue:#1a55c4;
  --text:#444;
  --link:#333;
  --rule:#0b2a63;
  --footer:#7b7b7b;
  --panel:#eeeeee;
  --white:#fff;
}
*{margin:0;padding:0;box-sizing:border-box}
html,body{width:1200px;height:762px;overflow:hidden}
body{font-family:"Arimo",Arial,sans-serif;color:var(--text);background:var(--white);position:relative}
.hero{position:absolute;left:0;top:0;width:1200px;height:220px;
  background:linear-gradient(90deg,#0a2150 0%,#0d2d6e 35%,#1446a8 60%,#0f3688 80%,#0a2352 100%)}
.hero-title{position:absolute;left:172px;top:128px;font-size:48px;font-weight:400;color:var(--white);letter-spacing:.5px}
.masthead{position:absolute;left:120px;top:0;width:960px;height:80px;background:linear-gradient(#fff 60%,#f4f4f4);border-radius:0 0 8px 8px}
.brand{position:absolute;left:8px;top:16px;display:flex;align-items:center;gap:10px}
.brand-mark{width:46px;height:46px;border-radius:50%;background:var(--navy)}
.brand-name{font-size:17px;font-weight:400;color:var(--navy);line-height:1.1}
.search{position:absolute;right:22px;top:12px;width:151px;height:21px;border-radius:11px;background:#f2f2f2;border:1px solid #e4e4e4}
.search span{position:absolute;left:8px;top:3px;font-size:13px;color:#aaa}
.search svg{position:absolute;right:-1px;top:-1px}
.nav{position:absolute;right:23px;top:50px;display:flex;gap:20px;list-style:none}
.nav li{font-size:14.5px;font-weight:700;color:var(--navy)}
.main{position:absolute;left:120px;top:240px;width:714px}
.section-title{font-size:18.5px;font-weight:700;color:var(--navy);padding-bottom:5px;border-bottom:4px solid var(--rule)}
.intro{display:flex;gap:20px;margin-top:9px}
.photo{width:348px;height:188px;border:3px solid #e2e2e2;background:linear-gradient(180deg,#b7d2ee 0%,#8d98a6 45%,#5b6068 80%,#9a9a96 100%);flex:none}
p{font-size:11.3px;line-height:14.3px;margin-bottom:14.3px}
.intro p{margin-top:1px}
.body-copy{margin-top:20px}
.sidebar{position:absolute;left:855px;top:240px;width:225px}
.sidebar .section-title{margin-bottom:9px}
.subnav{list-style:none;margin-bottom:32px}
.subnav li{font-size:12px;font-weight:700;color:var(--link);line-height:18px;padding-left:11px}
.subnav li.current{color:var(--navy);padding-left:1px}
.video{height:149px;background:var(--panel);margin-top:9px}
.video-title{font-size:14px;font-weight:700;color:var(--link);margin:18px 0 1px -2px}
.video-text{font-size:11.3px;line-height:14.3px;margin-left:-2px}
.video-text b{color:var(--navy);margin-left:4px}
.footer{position:absolute;left:0;top:730px;width:1200px;height:32px;background:var(--footer);color:var(--white);font-size:10px;text-align:center;line-height:32px}
.footer a{color:var(--white);margin-left:4px}
</style>
</head>
<body>
<div class="hero" role="img" aria-label="Deep blue banner with abstract brushed texture"></div>
<h1 class="hero-title">COMPANY</h1>

<header class="masthead">
  <div class="brand"><span class="brand-mark"></span><span class="brand-name">Orvane Trading Limited</span></div>
  <div class="search"><span>search</span>
    <svg width="27" height="23" viewBox="0 0 27 23"><rect width="27" height="23" rx="11.5" fill="#0b2a63"/><circle cx="12" cy="10" r="4.5" fill="none" stroke="#fff" stroke-width="2.2"/><line x1="15.2" y1="13.2" x2="19" y2="17" stroke="#fff" stroke-width="2.6" stroke-linecap="round"/></svg>
  </div>
  <ul class="nav"><li>Company</li><li>Our Business</li><li>Investor Relations</li><li>News Releases</li><li>Careers</li><li>Contact Us</li></ul>
</header>

<main class="main">
  <h2 class="section-title">Company Overview</h2>
  <div class="intro">
    <div class="photo" role="img" aria-label="Modern multi-storey office building under a blue sky"></div>
    <div>
      <p>Lorem ipsum dolor sit amet, consectetur adipiscing elit. Nunc ultricies nulla massa, ut sollicitudin dui vulputate nec. Nulla dolor tellus, aliquam a odio quis, vehicula porttitor dolor. Nam dignissim metus eget ante tempor, et commodo sem egestas. Morbi enim enim, tristique porttitor tellus lobortis, facilisis vehicula odio. Aenean vitae rutrum nunc. Aliquam sit amet leo sollicitudin, aliquam urna vitae, feugiat libero. Quisque vel porttitor nibh, sed porttitor dolor. Nulla dapibus luctus aliquet. Ut placerat ante et orci posuere molestie. Nulla in dictum lectus, in sagittis massa.</p>
      <p>Integer enim lorem, mollis sed justo vitae, condimentum hendrerit augue. Maecenas aliquet turpis ut placerat euismod. Duis ut cursus elit. Nunc eget sodales lectus.</p>
    </div>
  </div>
  <div class="body-copy">
    <p>Lorem ipsum dolor sit amet, consectetur adipiscing elit. Nunc ultricies nulla massa, ut sollicitudin dui vulputate nec. Nulla dolor tellus, aliquam a odio quis, vehicula porttitor dolor. Nam dignissim metus eget ante tempor, et commodo sem egestas. Morbi enim enim, tristique porttitor tellus lobortis, facilisis vehicula odio. Aenean vitae rutrum nunc. Aliquam sit amet leo sollicitudin, aliquam urna vitae, feugiat libero. Quisque vel porttitor nibh, sed porttitor dolor. Nulla dapibus luctus aliquet. Ut placerat ante et orci posuere molestie. Nulla in dictum lectus, in sagittis massa.</p>
    <p>Integer enim lorem, mollis sed justo vitae, condimentum hendrerit augue. Maecenas aliquet turpis ut placerat euismod. Duis ut cursus elit. Nunc eget sodales lectus. Vestibulum sed cursus orci. Class aptent taciti sociosqu ad litora torquent per conubia nostra, per inceptos himenaeos. Curabitur ultricies ornare purus et pretium.</p>
    <p>Mauris aliquam molestie metus ut bibendum. Quisque sit amet egestas risus. Praesent pulvinar, erat vitae ultrices porttitor, nibh velit varius justo, in pretium dolor nisi et orci. Mauris consectetur mi ut egestas mattis. Aenean eu velit eu quam condimentum cursus. Phasellus eleifend augue et enim interdum, non imperdiet sem laoreet. Quisque libero leo, pretium at dapibus vel, hendrerit sed est. Nam ullamcorper tortor id aliquet lacinia. Maecenas feugiat sapien eu nisl pharetra euismod. Praesent sit amet mauris convallis, vehicula leo id, adipiscing enim. Nulla facilisi. Praesent eget tempor elit, quis congue metus.</p>
  </div>
</main>

<aside class="sidebar">
  <h2 class="section-title">Company</h2>
  <ul class="subnav">
    <li class="current">&gt; Company Overview</li>
    <li>Board of Directors</li>
    <li>Organization &amp; Management</li>
  </ul>
  <h2 class="section-title">Our Video</h2>
  <div class="video" role="img" aria-label="Company video preview"></div>
  <h3 class="video-title">Lorem ipsum dolor sit amet</h3>
  <p class="video-text">Lorem ipsum dolor sit amet, consectetur adipisicing elit, sed do eiusmod tempor incididunt ut labore et dolore magna <b>[+]</b></p>
</aside>

<footer class="footer">© Copyright 2014 Orvane Trading Limited. All rights reserved. <a href="#">Disclaimer and Privacy Statement</a></footer>
</body>
</html>
```